Vornexa Ad Banners for Car Buying Service

We offer a fast, safe way for car owners to sell their car. They load the car details on our site, we give them a cash offer. If interested, we visit them and conclude deal, same day payment.
I want subtle animated banners for our Vornexa Display ads. (Dimensions - 120x600 - 160x600 - 300x250 - 300x600 - 320 x 50 - 728x90)
We can discuss messaging. I will attach recent static banners we had designed - and an older HTML5 animated version.
I'm looking for something subtle, modern but with clear call to action.
Target Market(s)
Car owners, male and female - wanting an easy, no fuss way to sell their car for cash
Industry/Entity Type
Automotive

```html
<!DOCTYPE html>
<html lang="en">
<head>
<meta charset="utf-8">
<title>Motorquay – We Want Your Car More</title>
<link href="https://fonts.googleapis.com/css2?family=Montserrat:wght@800;900&display=swap" rel="stylesheet">
<style>
  :root {
    --page: #dde1e7;
    --card-top: #fbfbfb;
    --card-bottom: #c8ced7;
    --brand-blue: #03a1e2;
    --brand-blue-deep: #0a5b82;
    --brand-green: #a1ad45;
    --ink: #050505;
    --white: #ffffff;
  }
  * { margin: 0; padding: 0; box-sizing: border-box; }
  html, body {
    width: 1200px;
    height: 825px;
    overflow: hidden;
    background: var(--page);
    font-family: "Montserrat", Arial, sans-serif;
  }
  .banner {
    position: absolute;
    left: 0;
    top: 112px;
    width: 1200px;
    height: 600px;
    border-radius: 14px;
    overflow: hidden;
    background: linear-gradient(180deg, var(--card-top) 0%, var(--card-bottom) 100%);
  }
  .banner-shapes {
    position: absolute;
    inset: 0;
    width: 1200px;
    height: 600px;
  }
  .headline {
    position: absolute;
    left: 121px;
    color: var(--ink);
    font-weight: 900;
    font-size: 59px;
    line-height: 1;
    letter-spacing: 0;
    white-space: nowrap;
  }
  .headline--want { top: 47px; }
  .headline--do { top: 252px; }
  .headline--help { top: 321px; }
  .headline--more {
    top: 131px;
    left: 118px;
    font-size: 90px;
    color: var(--white);
    text-shadow: 3px 5px 8px rgba(0, 40, 70, 0.45);
  }
  .bullet {
    position: absolute;
    left: 65px;
    width: 31px;
    height: 31px;
  }
  .bullet--want { top: 58px; }
  .bullet--more { top: 171px; width: 28px; height: 28px; left: 67px; }
  .bullet--do { top: 262px; }
  .bullet--help { top: 331px; }
  .car-photo {
    position: absolute;
    left: 534px;
    top: 271px;
    width: 592px;
    height: 298px;
    border-radius: 48% 40% 30% 30% / 40% 40% 22% 22%;
    background: radial-gradient(ellipse at 45% 40%, #4a4a4a 0%, #222 45%, #0e0e0e 100%);
  }
  .brand-name {
    position: absolute;
    left: 140px;
    top: 490px;
    display: flex;
    align-items: center;
    gap: 12px;
    color: var(--white);
    font-weight: 800;
    font-size: 40px;
    line-height: 1;
    white-space: nowrap;
  }
  .brand-name__dot {
    width: 16px;
    height: 16px;
    border-radius: 50%;
    background: var(--brand-blue);
  }
</style>
</head>
<body>
  <main class="banner">
    <svg class="banner-shapes" viewBox="0 0 1200 600" aria-hidden="true">
      <defs>
        <linearGradient id="lowerStripe" x1="0" y1="1" x2="0.4" y2="0">
          <stop offset="0" stop-color="#06405f"/>
          <stop offset="1" stop-color="#0a6a96"/>
        </linearGradient>
        <linearGradient id="lowerPanel" x1="0" y1="0" x2="0" y2="1">
          <stop offset="0" stop-color="#111"/>
          <stop offset="1" stop-color="#000"/>
        </linearGradient>
      </defs>

      <path d="M1010,0 H1090 C1080,120 1040,200 985,274 L905,272 C960,200 1000,120 1010,0 Z" fill="var(--brand-green)"/>
      <path d="M1090,0 H1186 Q1200,0 1200,16 C1192,120 1140,220 1071,301 L985,274 C1040,200 1080,120 1090,0 Z" fill="var(--brand-blue)"/>

      <path d="M0,600 C40,460 190,400 460,400 H600 L985,274 L1071,301 C1140,220 1192,120 1200,16 V600 Z" fill="url(#lowerStripe)"/>
      <path d="M0,600 C50,480 200,420 460,420 H600 L1000,300 L1071,301 C1140,220 1192,120 1200,40 V600 Z" fill="url(#lowerPanel)"/>

      <path d="M560,126 H700 Q718,126 708,146 C670,202 622,229 574,229 H520 Z" fill="var(--brand-green)"/>
      <path d="M0,163 C20,138 42,126 66,126 H628 Q646,126 636,144 C604,198 566,226 522,229 H66 C40,229 14,248 0,279 Z" fill="var(--brand-blue)"/>
    </svg>

    <svg class="bullet bullet--want" viewBox="0 0 24 24" aria-hidden="true"><path d="M12 2.5l2.9 6 6.6.8-4.9 4.5 1.3 6.5L12 17l-5.9 3.3 1.3-6.5-4.9-4.5 6.6-.8z" fill="var(--brand-blue)" stroke="var(--brand-blue)" stroke-width="1.5" stroke-linejoin="round"/></svg>
    <svg class="bullet bullet--more" viewBox="0 0 24 24" aria-hidden="true"><path d="M12 2.5l2.9 6 6.6.8-4.9 4.5 1.3 6.5L12 17l-5.9 3.3 1.3-6.5-4.9-4.5 6.6-.8z" fill="var(--white)" stroke="var(--white)" stroke-width="1.5" stroke-linejoin="round"/></svg>
    <svg class="bullet bullet--do" viewBox="0 0 24 24" aria-hidden="true"><path d="M12 2.5l2.9 6 6.6.8-4.9 4.5 1.3 6.5L12 17l-5.9 3.3 1.3-6.5-4.9-4.5 6.6-.8z" fill="var(--brand-blue)" stroke="var(--brand-blue)" stroke-width="1.5" stroke-linejoin="round"/></svg>
    <svg class="bullet bullet--help" viewBox="0 0 24 24" aria-hidden="true"><path d="M12 2.5l2.9 6 6.6.8-4.9 4.5 1.3 6.5L12 17l-5.9 3.3 1.3-6.5-4.9-4.5 6.6-.8z" fill="var(--brand-blue)" stroke="var(--brand-blue)" stroke-width="1.5" stroke-linejoin="round"/></svg>

    <h1 class="headline headline--want">WE WANT YOUR CAR</h1>
    <p class="headline headline--more">MORE!</p>
    <p class="headline headline--do">WE DO</p>
    <p class="headline headline--help">WE HELP</p>

    <div class="car-photo" role="img" aria-label="Photo of a glossy black sports sedan, front three-quarter view, with silver alloy wheels"></div>

    <div class="brand-name"><span class="brand-name__dot"></span>Motorquay.co.za</div>
  </main>
</body>
</html>
```